Business Card

I need a business card that really pops for a potential customer or person who refers a personal injury lead. I want to highlight our office locations, but only address that needs to be on the card is my office's main address. I want a sleek, modern and minimalist design.

```html
<!DOCTYPE html>
<html lang="en">
<head>
<meta charset="utf-8">
<title>Prairie Injury Group — Business Card</title>
<link rel="stylesheet" href="https://fonts.googleapis.com/css2?family=Arimo:wght@400;700&family=Jost:wght@400&display=swap">
<style>
  :root {
    --bg: #d9d9d9;
    --card-dark: #3a3a3a;
    --card-light: #ffffff;
    --accent-grey: #8c8c8c;
    --ink-light: #f4f4f4;
    --ink-dark: #2c2c2c;
    --silver: #a3a3a3;
  }
  * { margin: 0; padding: 0; box-sizing: border-box; }
  html, body { width: 1200px; height: 800px; overflow: hidden; }
  body {
    background: var(--bg);
    position: relative;
    font-family: "Arimo", Arial, sans-serif;
  }
  .card {
    position: absolute;
    top: 246px;
    width: 540px;
    height: 308px;
    border-radius: 22px;
    background: var(--card-dark);
    overflow: hidden;
    box-shadow: 0 10px 24px rgba(0,0,0,0.18);
  }
  .card--front { left: 40px; }
  .card--back { left: 620px; }

  .front-panel { position: absolute; inset: 0; }

  .wordmark {
    font-family: "Jost", Arial, sans-serif;
    font-weight: 400;
    letter-spacing: 0.02em;
    white-space: nowrap;
  }
  .front-wordmark {
    position: absolute;
    left: 290px;
    top: 142px;
    width: 230px;
    text-align: center;
    font-size: 18px;
    line-height: 24px;
    color: var(--ink-dark);
  }

  .contact {
    position: absolute;
    left: 30px;
    top: 52px;
    color: var(--ink-light);
  }
  .contact__name { font-size: 22px; font-weight: 700; line-height: 1.1; }
  .contact__role { font-size: 13px; margin-top: 2px; }
  .contact__address { font-size: 13px; line-height: 1.35; margin-top: 30px; }
  .contact__list { list-style: none; margin-top: 18px; font-size: 13px; line-height: 1.35; }
  .contact__list li { display: flex; align-items: center; gap: 7px; }
  .contact__list svg { width: 11px; height: 11px; flex: none; }

  .back-wordmark {
    position: absolute;
    inset: 0;
    display: flex;
    align-items: center;
    justify-content: center;
    font-size: 34px;
    color: var(--silver);
  }
</style>
</head>
<body>

<section class="card card--front" aria-label="Business card front">
  <svg class="front-panel" viewBox="0 0 540 308" aria-hidden="true">
    <polygon points="318,-10 540,-10 540,318 318,318 238,154" fill="var(--accent-grey)" stroke="var(--accent-grey)" stroke-width="14" stroke-linejoin="round"/>
    <polygon points="334,-10 550,-10 550,318 334,318 254,154" fill="var(--card-light)" stroke="var(--card-light)" stroke-width="14" stroke-linejoin="round"/>
  </svg>
  <div class="wordmark front-wordmark">Prairie Injury Group</div>

  <div class="contact">
    <p class="contact__name">Daniel Harper</p>
    <p class="contact__role">Lawyer</p>
    <p class="contact__address">480 Harbor Point Avenue<br>Suite 3100<br>Riverton, IL 60610</p>
    <ul class="contact__list">
      <li>
        <svg viewBox="0 0 12 12" aria-hidden="true"><path d="M2.5 1h2l1 3-1.3 1a6 6 0 0 0 2.8 2.8L8 6.5l3 1v2a1.5 1.5 0 0 1-1.5 1.5A8.5 8.5 0 0 1 1 2.5 1.5 1.5 0 0 1 2.5 1z" fill="currentColor"/></svg>
        312-555-0142
      </li>
      <li>
        <svg viewBox="0 0 12 12" aria-hidden="true"><rect x="2" y="1" width="8" height="10" rx="1" fill="currentColor"/><rect x="3.5" y="3" width="5" height="1" fill="var(--card-dark)"/><rect x="3.5" y="5.5" width="5" height="1" fill="var(--card-dark)"/><rect x="3.5" y="8" width="5" height="1" fill="var(--card-dark)"/></svg>
        312-555-0187
      </li>
      <li>
        <svg viewBox="0 0 12 12" aria-hidden="true"><rect x="1" y="2.5" width="10" height="7" rx="1" fill="currentColor"/><path d="M1.5 3l4.5 3.5L10.5 3" fill="none" stroke="var(--card-dark)" stroke-width="1"/></svg>
        info@prairieinjurygroup.com
      </li>
      <li>
        <svg viewBox="0 0 12 12" aria-hidden="true"><circle cx="6" cy="6" r="5" fill="currentColor"/><path d="M1 6h10M6 1c-2 2.5-2 7.5 0 10M6 1c2 2.5 2 7.5 0 10" fill="none" stroke="var(--card-dark)" stroke-width="0.8"/></svg>
        prairieinjurygroup.com
      </li>
    </ul>
  </div>
</section>

<section class="card card--back" aria-label="Business card back">
  <div class="wordmark back-wordmark">Prairie Injury Group</div>
</section>

</body>
</html>
```